Business Card Design for a Jockey's Agent

A business card design that helps to develop a brand or identity for myself, the agent, perhaps on one side with a clean minimalist design, and on the other side a simple design with the two jockeys names i currently represent. Those jockeys may change twice a year as they move around the country, switch agents, etc, so i think keeping one side designed to promote the agent and a second side that can be changed easily to identify the jockeys i currently represent would be the best.

Target Market(s)

Thoroughbred racehorse trainers

Industry/Entity Type

Business

Contact Information for Business Card

Gareth Lindqvist - Jockey Agent
mobile (555) 813 2649
garethklindqvist2fenmail.com

Jockeys: Tobias Wren, Marlow Pendry

Font styles to use
Serif

Requirements
Must have
• contact info and modern feel and font
Nice to have
• clean minimalist element of racing, jockey silk, helmut or crop, finish marker pole from racetrack etc,
Should not have
• DONT HAVE ANY KIND OF LOGO ETC. IMAGE IS ONE OF MY RACEHORSES TO HELP FINISH BRIEF.
• racing horse, stuffy vintage racing feel or Weekly Paddock Sheet fonts

```html
<!DOCTYPE html>
<html lang="en">
<head>
<meta charset="utf-8">
<title>Gareth Lindqvist – Jockey Agent Business Card</title>
<link rel="stylesheet" href="https://fonts.googleapis.com/css2?family=Cinzel:wght@400;500&family=Caladea&family=Carlito:wght@400;700&display=swap">
<style>
  :root {
    --page-bg: #ece9e4;
    --royal: #2148b0;
    --royal-deep: #1a3a96;
    --royal-light: #3a66c8;
    --navy-text: #1f3590;
    --paper: #ffffff;
    --paper-shade: #eeeeee;
    --rule-grey: #7a7a7a;
    --silhouette: #d9dde6;
  }
  * { box-sizing: border-box; margin: 0; padding: 0; }
  html, body {
    width: 1200px; height: 912px; overflow: hidden;
    background: var(--page-bg);
  }
  .stage {
    position: relative; width: 1200px; height: 912px;
    display: flex; align-items: center; justify-content: center; gap: 60px;
  }
  .card {
    position: relative; width: 500px; height: 300px; overflow: hidden;
    box-shadow: 0 6px 18px rgba(0,0,0,0.25);
  }

  /* Back side */
  .card-back {
    background: radial-gradient(ellipse at 55% 40%, var(--royal-light) 0%, var(--royal) 45%, var(--royal-deep) 100%);
  }
  .card-back .rider-watermark {
    position: absolute; left: 0; top: 80px; width: 270px; height: 220px;
    background: radial-gradient(ellipse at 40% 60%, rgba(255,255,255,0.16), rgba(255,255,255,0.03) 70%, transparent 100%);
    border-radius: 40% 60% 0 0;
  }

  /* Front side */
  .card-front {
    background: linear-gradient(180deg, var(--paper) 30%, var(--paper-shade) 100%);
    font-family: "Carlito", "Calibri", sans-serif;
  }
  .header-band {
    position: absolute; left: 0; top: 0; width: 100%; height: 102px;
    background: linear-gradient(180deg, var(--royal-deep) 0%, var(--royal) 60%, var(--royal-light) 100%);
  }
  .header-rule {
    position: absolute; left: 0; top: 107px; width: 100%; height: 3px;
    background: var(--royal);
  }
  .racing-art {
    position: absolute; left: 4px; top: 14px; width: 136px; height: 78px;
    background: linear-gradient(90deg, rgba(255,255,255,0.55), var(--silhouette));
    border-radius: 45% 55% 30% 30%;
    opacity: 0.85;
  }
  .agent-identity {
    position: absolute; left: 140px; top: 14px; width: 260px; text-align: center; color: var(--paper);
  }
  .agent-name {
    font-family: "Cinzel", "Trajan Pro", serif; font-weight: 500;
    font-size: 26px; letter-spacing: 0.5px; line-height: 1;
    padding: 4px 0 5px;
    border-top: 2px solid var(--paper);
    border-bottom: 2px solid var(--paper);
    margin-top: 4px;
  }
  .agent-title {
    font-size: 17px; margin-top: 12px; letter-spacing: 0.3px;
  }
  .jockey-roster {
    position: absolute; left: 20px; top: 160px; color: var(--navy-text);
  }
  .roster-label { font-size: 18px; font-weight: 700; }
  .roster-names {
    list-style: none; margin: 6px 0 0 33px;
    font-family: "Caladea", "Cambria", serif; font-size: 21px; line-height: 26px;
  }
  .card-divider {
    position: absolute; left: 254px; top: 138px; width: 1px; height: 138px;
    background: var(--rule-grey);
  }
  .contact-list {
    position: absolute; left: 300px; top: 170px; list-style: none;
    color: var(--navy-text); font-size: 12px;
  }
  .contact-list li { display: flex; align-items: center; gap: 6px; height: 18px; }
  .contact-list svg { width: 11px; height: 11px; flex: none; }
  .contact-list .social-dot {
    width: 9px; height: 9px; border-radius: 50%; background: var(--navy-text); margin: 0 1px; flex: none;
  }
</style>
</head>
<body>
<main class="stage">
  <section class="card card-back" aria-label="Card back">
    <div class="rider-watermark" role="img" aria-label="Faint silhouette of a jockey on a racehorse"></div>
  </section>

  <section class="card card-front" aria-label="Card front">
    <div class="header-band"></div>
    <div class="header-rule"></div>
    <div class="racing-art" role="img" aria-label="Silhouettes of two racehorses with jockeys at full gallop"></div>
    <div class="agent-identity">
      <h1 class="agent-name">Gareth Lindqvist</h1>
      <p class="agent-title">Jockey Agent</p>
    </div>

    <div class="jockey-roster">
      <p class="roster-label">Jockeys:</p>
      <ul class="roster-names">
        <li>Tobias Wren</li>
        <li>Marlow Pendry</li>
      </ul>
    </div>

    <div class="card-divider"></div>

    <ul class="contact-list">
      <li>
        <svg viewBox="0 0 12 12" aria-hidden="true"><circle cx="6" cy="6" r="5.2" fill="none" stroke="currentColor" stroke-width="1.2"/><path d="M4 3.2l1 1.5-.6.7c.4.9 1.1 1.6 2 2l.7-.6 1.5 1-.6 1c-2.3-.3-4.4-2.4-4.7-4.7z" fill="currentColor"/></svg>
        <span>(555) 813 2649</span>
      </li>
      <li>
        <svg viewBox="0 0 12 12" aria-hidden="true"><rect x="1" y="3" width="10" height="7" fill="currentColor"/><path d="M1 3l5 4 5-4" fill="none" stroke="#fff" stroke-width="1"/></svg>
        <span>garethklindqvist@fenmail.com</span>
      </li>
      <li><span class="social-dot"></span><span>Garethlindqvist</span></li>
      <li><span class="social-dot"></span><span>@Garethlindqvist</span></li>
    </ul>
  </section>
</main>
</body>
</html>
```